Business Card Design for a Software Startup

We'd like to have a business card design. We already have a logo. Basically what we need is a clean design with name, address, cellphone and phone numbers, e-mail and web site address (front) and a space on the back with our logo with the company name on the right side and some texts on the bottom.
We are a development and consulting company in Brazil with highly qualified team of professionals in Java, iOS and Android development and consulting.

Target Market(s)

CIO, IT managers of mid to big size companies

Industry/Entity Type

Business

```html
<!DOCTYPE html>
<html lang="en">
<head>
<meta charset="utf-8">
<title>NUVEXA Business Card</title>
<link rel="stylesheet" href="https://fonts.googleapis.com/css2?family=Open+Sans:wght@400;600;700&display=swap">
<style>
  :root {
    --page-bg: #e4e6ea;
    --card-white: #ffffff;
    --brand-navy: #1d4e8f;
    --brand-deep: #0c2c4f;
    --brand-mid: #1a5488;
    --wave-light: #1aa3e0;
    --wave-dark: #2b3a7c;
    --text-dark: #2d2d33;
    --divider: #cfd3d9;
  }
  * { margin: 0; padding: 0; box-sizing: border-box; }
  html, body {
    width: 1200px; height: 987px; overflow: hidden;
    background: var(--page-bg);
    font-family: "Open Sans", sans-serif;
  }
  .canvas { position: relative; width: 1200px; height: 987px; }
  .card {
    position: absolute; left: 320px; width: 560px; height: 320px;
    border-radius: 22px; overflow: hidden;
    box-shadow: 0 6px 18px rgba(0,0,0,0.12);
  }
  .card-front { top: 140px; background: var(--card-white); }
  .card-back {
    top: 527px;
    background: radial-gradient(ellipse at 50% 45%, var(--brand-mid) 0%, var(--brand-deep) 75%);
  }
  .wave { position: absolute; left: 0; top: 0; }
  .brand {
    position: absolute; left: 40px; top: 40px;
    display: flex; align-items: center; gap: 14px;
  }
  .brand-square { width: 56px; height: 56px; background: var(--brand-navy); }
  .brand-name {
    font-weight: 700; font-size: 34px; color: var(--brand-navy); letter-spacing: 1px;
  }
  .divider {
    position: absolute; left: 285px; top: 40px; width: 1px; height: 150px;
    background: var(--divider);
  }
  .contact { position: absolute; left: 305px; top: 36px; color: var(--text-dark); }
  .contact-name { font-weight: 700; font-size: 26px; color: var(--brand-navy); line-height: 1.1; }
  .contact-title { font-size: 15px; margin-bottom: 12px; }
  .contact-row { display: flex; align-items: center; gap: 8px; font-size: 15px; line-height: 22px; }
  .contact-row svg { width: 13px; height: 13px; flex: none; }
  .address {
    position: absolute; right: 40px; top: 250px; text-align: right;
    color: var(--card-white); font-size: 15px; line-height: 22px;
  }
  .back-brand {
    position: absolute; left: 0; right: 0; top: 120px;
    display: flex; justify-content: center; align-items: center; gap: 16px;
  }
  .back-brand .brand-square { width: 48px; height: 48px; background: var(--card-white); }
  .back-brand .brand-name { color: var(--card-white); font-size: 40px; }
  .back-web {
    position: absolute; left: 0; right: 0; top: 250px; text-align: center;
    color: var(--card-white); font-size: 15px; letter-spacing: 4px;
  }
</style>
</head>
<body>
<main class="canvas">
  <section class="card card-front">
    <svg class="wave" width="560" height="320" viewBox="0 0 560 320">
      <defs>
        <linearGradient id="waveFill" x1="0" y1="0" x2="1" y2="1">
          <stop offset="0" stop-color="var(--wave-light)"/>
          <stop offset="1" stop-color="var(--wave-dark)"/>
        </linearGradient>
      </defs>
      <path d="M0,100 C30,190 160,210 300,215 C430,220 520,240 560,280 L560,320 L0,320 Z" fill="url(#waveFill)"/>
      <path d="M0,130 C40,205 170,222 300,228 C420,234 510,255 560,300" fill="none" stroke="#ffffff" stroke-width="3"/>
      <path d="M0,100 C30,190 160,210 300,215 C430,220 520,240 560,280" fill="none" stroke="var(--wave-dark)" stroke-width="3"/>
    </svg>

    <div class="brand">
      <div class="brand-square"></div>
      <span class="brand-name">NUVEXA</span>
    </div>

    <div class="divider"></div>

    <div class="contact">
      <div class="contact-name">Your Name</div>
      <div class="contact-title">Title</div>
      <div class="contact-row">
        <svg viewBox="0 0 16 16"><circle cx="8" cy="8" r="7" fill="none" stroke="var(--text-dark)" stroke-width="1.5"/><path d="M5 4.5l2 2-1 1c.5 1 1.5 2 2.5 2.5l1-1 2 2-1.3 1.3C7 12 4 9 3.7 5.8z" fill="var(--text-dark)"/></svg>
        <span>123-456-7890</span>
      </div>
      <div class="contact-row">
        <svg viewBox="0 0 16 16"><rect x="4" y="1" width="8" height="14" rx="1.5" fill="var(--text-dark)"/><rect x="5.5" y="3" width="5" height="6" fill="#fff"/></svg>
        <span>456-085-4321</span>
      </div>
      <div class="contact-row">
        <svg viewBox="0 0 16 16"><rect x="1" y="3" width="14" height="10" rx="1" fill="var(--text-dark)"/><path d="M1.5 3.5L8 9l6.5-5.5" fill="none" stroke="#fff" stroke-width="1.3"/></svg>
        <span>yourname@nuvexa.com</span>
      </div>
      <div class="contact-row">
        <svg viewBox="0 0 16 16"><circle cx="8" cy="8" r="7" fill="none" stroke="var(--text-dark)" stroke-width="1.4"/><ellipse cx="8" cy="8" rx="3" ry="7" fill="none" stroke="var(--text-dark)" stroke-width="1.2"/><path d="M1 8h14M2.5 4.5h11M2.5 11.5h11" stroke="var(--text-dark)" stroke-width="1.1"/></svg>
        <span>www.nuvexa.com</span>
      </div>
    </div>

    <div class="address">
      <div>Door No. Street Name</div>
      <div>City Name, State, Zip Code</div>
    </div>
  </section>

  <section class="card card-back">
    <div class="back-brand">
      <div class="brand-square"></div>
      <span class="brand-name">NUVEXA</span>
    </div>
    <div class="back-web">www.nuvexa.com</div>
  </section>
</main>
</body>
</html>
```